I need a website for my moving company Bolt Hauling LLC. I would like the following text included in my website. I have purchased the domain bolthaulingcrew.example from siteburrow.example. I am not familiar with SEO or other techniques that help my page on search engines but would like the website to be optimized for Findora search engine. I have attached our logo below and would like it to be used in the design. The colors in the logo can be used also in the design.
Home/About Us
At Bolt Hauling LLC, we know moving. It can be difficult, stressful, and a real pain in the backside. But it doesn’t have to be! When you partner with Bolt, you get the benefits of a professional moving team that is licensed and insured for your protection along with years of experience and a dedication to providing the highest quality service, each and every time.
Our Services
We do a wide variety of local moves, including apartments, single-family homes, retirement communities, dorms, condos, and many more! Our movers are trained to protect your belongings and your home – all pieces of furniture are padded and stretch wrapped free of charge, ensuring your items and home are damage-free at the end of your move. Having added stress about packing up your home prior to moving? We’ve got you covered with our full service packing and unpacking services, too.
What You Get
When you partner with BOLT, you’ll get the best service in the industry, as well as:
* The Use of Packing & Moving Materials: The hourly rate includes the use of our dollies, ratchet straps, pads, moving tools, and property protection like floor mats, door-jamb protectors, stairwell protectors, and plenty of muscle!
• Trained, Licensed, and Insured Movers: All of our movers are highly trained to provide you with the best service, and to ensure the protection of you and your items.
• Professional: Honest, Uniformed, Nice, Knowledgeable Service is what you’ll get with every member of our moving teams.
• Custom Service for Every Move: Every move is as unique as the person or business moving. Our training and equipment allows us to customize every project to ensure the very best for every client.
Target Market(s)
Home and Business movers
Industry/Entity Type
Moving Company
Colors
Designer to choose colors to be used in the design.
Requirements
Must have
- 2 sides
Nice to have
- Colorful design with logo included.
Should not have
- animated characters

```html
<!DOCTYPE html>
<html lang="en">
<head>
<meta charset="utf-8">
<title>Bolt Hauling LLC – Moving Company</title>
<link rel="stylesheet" href="https://fonts.googleapis.com/css2?family=Roboto+Slab:wght@300;400;700&display=swap">
<style>
:root{
  --orange:#f39220;
  --orange-dark:#e07f10;
  --green:#8dc63f;
  --green-dark:#74ad2b;
  --ink:#222;
  --text:#555;
  --white:#fff;
  --footer:#2a1f18;
}
*{box-sizing:border-box;margin:0;padding:0}
html,body{width:1200px;height:3061px;overflow:hidden}
body{position:relative;background:var(--white);font-family:"Roboto Slab",serif;color:var(--text)}
.abs{position:absolute}

/* header */
.site-header{left:0;top:0;width:1200px;height:112px;border-top:5px solid var(--green);background:var(--white)}
.brand{left:96px;top:30px;display:flex;align-items:center;gap:12px;font-weight:700;font-size:26px;color:var(--orange)}
.brand-mark{width:34px;height:34px;background:var(--green);border-radius:50%}
.main-nav{right:122px;top:36px;display:flex;align-items:center;gap:34px;font-size:15px;color:var(--ink)}
.btn{display:inline-flex;align-items:center;gap:8px;background:var(--orange);color:var(--white);border-radius:24px;font-weight:700;text-transform:uppercase}
.main-nav .btn{padding:12px 24px;font-size:13px}

/* hero */
.hero{left:0;top:112px;width:1200px;height:530px;background:linear-gradient(110deg,#a27a52 0%,#c9a27a 35%,#e4c9a6 60%,#8e6c4e 100%)}
.hero-title{left:98px;top:80px;color:var(--white);font-size:28px;font-weight:700}
.booking-card{left:100px;top:145px;width:295px;height:255px;background:rgba(255,255,255,.93);border:4px solid rgba(255,255,255,.6);outline:1px solid #ccc;outline-offset:-12px;text-align:center;padding-top:40px}
.booking-card h3{font-size:21px;color:var(--ink)}
.booking-card .svc{color:var(--green);font-size:18px;margin-top:22px}
.booking-card .meta{font-size:12px;margin-top:16px}
.booking-card .btn{padding:10px 22px;font-size:11px;margin-top:18px}
.hero-arrow{top:245px}
.hero-curve{left:0;top:548px}

/* sections */
.section-title{width:1200px;left:0;text-align:center;font-size:36px;font-weight:700;color:var(--ink)}
.lead{left:230px;width:740px;text-align:center;font-size:12px;line-height:28px}
.photo-circle{width:232px;height:232px;border-radius:50%;border:6px solid var(--white);box-shadow:0 0 0 1px #ddd}
.services{left:0;top:1168px;width:1200px;height:440px;background:linear-gradient(180deg,#f7a033,#f08d18)}
.services .section-title{color:var(--white);top:94px}
.services .lead{top:158px;color:var(--white);left:200px;width:800px}
.call{left:0;width:1200px;top:292px;display:flex;justify-content:center;align-items:center;gap:14px;color:var(--white);font-size:26px;font-weight:700}
.call-icon{width:46px;height:46px;border:2px solid var(--white);border-radius:50%;display:flex;align-items:center;justify-content:center}

.perk-link{color:var(--orange)}
.feature{width:300px;text-align:center}
.feature-ring{width:208px;height:208px;border-radius:50%;border:8px solid var(--green);margin:0 auto;display:flex;align-items:center;justify-content:center}
.feature-art{width:130px;height:110px;border-radius:16px;background:linear-gradient(#f6a341,#ef8a18)}
.feature h3{font-size:20px;font-weight:400;color:var(--ink);margin-top:68px;line-height:30px}
.feature p{font-size:12px;line-height:26px;margin-top:10px}
.divider{width:1px;height:60px;background:#e4e4e4;top:1940px}

/* footer */
.site-footer{left:0;top:2490px;width:1200px;height:571px;background:linear-gradient(160deg,#3a2b20,#1f1712 60%,#2d221a)}
.footer-curve{left:0;top:2470px}
.newsletter{left:215px;top:2404px;width:770px;height:200px;background:var(--green);text-align:center;color:var(--white);padding-top:30px}
.newsletter h2{font-size:28px}
.newsletter p{font-size:12px;margin-top:12px}
.subscribe-form{display:flex;width:560px;margin:16px auto 0;height:42px}
.subscribe-form span{flex:1;background:var(--white);border-radius:22px 0 0 22px;text-align:left;padding:12px 22px;color:#aaa;font-size:12px;font-style:italic}
.subscribe-form b{background:var(--orange);border-radius:0 22px 22px 0;padding:13px 22px;font-size:13px}
.footer-col h4{color:var(--white);font-size:22px;font-weight:700}
.contact-row{display:flex;gap:16px;align-items:center;color:#ddd;font-size:13px;line-height:22px;margin-top:18px}
.ring-icon{width:46px;height:46px;border:2px solid var(--white);border-radius:50%;display:flex;align-items:center;justify-content:center;flex:none}
.quick-links li{list-style:none;color:#ddd;font-size:13px;margin-top:22px}
.map{left:670px;top:2734px;width:420px;height:178px;background:linear-gradient(135deg,#e8e6df,#d7e3e8)}
.copyright{left:108px;top:3012px;color:#ccc;font-size:12px}
.footer-rule{left:108px;top:2985px;width:984px;height:1px;background:rgba(255,255,255,.15)}
.social-dot{left:1048px;top:2997px;width:40px;height:40px;border-radius:50%;background:#3b5998}
</style>
</head>
<body>

<header class="site-header abs">
  <div class="brand abs"><span class="brand-mark"></span>Bolt Hauling</div>
  <nav class="main-nav abs">
    <span>Home</span><span>About Us</span><span>Our Services</span><span>What You Get</span><span>Contact Us</span>
    <span class="btn">
      <svg width="13" height="13" viewBox="0 0 14 14" fill="none" stroke="#fff" stroke-width="1.6"><rect x="1" y="3" width="10" height="10"/><path d="M6 8l7-7"/></svg>Book Today</span>
  </nav>
</header>

<section class="hero abs" role="img" aria-label="Photo of a smiling couple sitting among cardboard moving boxes">
  <h1 class="hero-title abs">Bolt Hauling LLC Fernbrook</h1>
  <div class="booking-card abs">
    <h3>Book an Appointment</h3>
    <div class="svc">Moving Service</div>
    <div class="meta">1 hour &nbsp;|&nbsp; $125.00</div>
    <span class="btn">Book Now</span>
  </div>
  <svg class="hero-arrow abs" style="left:40px" width="24" height="44" viewBox="0 0 24 44"><path d="M22 2L2 22l20 20" fill="none" stroke="#fff" stroke-width="2"/></svg>
  <svg class="hero-arrow abs" style="right:40px" width="24" height="44" viewBox="0 0 24 44"><path d="M2 2l20 20L2 42" fill="none" stroke="#fff" stroke-width="2"/></svg>
</section>
<svg class="hero-curve abs" width="1200" height="96" viewBox="0 0 1200 96">
  <path d="M0 96V90C300 20 800 20 1200 62V96Z" fill="#fff"/>
  <path d="M0 90C300 20 800 20 1200 62" fill="none" stroke="#8dc63f" stroke-width="6"/>
</svg>

<h2 class="section-title abs" style="top:678px">About Bolt Hauling LLC</h2>
<p class="lead abs" style="top:738px">At Bolt Hauling LLC, we know moving. It can be difficult, stressful, and a real pain in the backside. But it doesn't have to be! When you partner with Bolt, you get the benefits of a professional moving team that is licensed and insured for your protection along with years of experience and a dedication to providing the highest quality service, each and every time.</p>
<div class="photo-circle abs" style="left:200px;top:858px;background:radial-gradient(#e6e0d8,#7d9cc0)" role="img" aria-label="Photo of a mover carrying a box"></div>
<div class="photo-circle abs" style="left:484px;top:858px;background:linear-gradient(#b9cde4,#7a9a6a 60%,#666)" role="img" aria-label="Photo of a moving truck on a mountain road"></div>
<div class="photo-circle abs" style="left:766px;top:858px;background:radial-gradient(#d9a765,#b6824b)" role="img" aria-label="Photo of a couple on the floor among boxes"></div>

<section class="services abs" role="img" aria-label="Orange-tinted photo of movers at work">
  <h2 class="section-title abs">Our Services</h2>
  <p class="lead abs">Bolt Hauling LLC in Fernbrook does a wide variety of local moves, including apartments, single-family homes, retirement communities, dorms, condos, and many more! Our movers are trained to protect your belongings and your home – all pieces of furniture are padded and stretch wrapped free of charge, ensuring your items and home are damage-free at the end of your move. Having added stress about packing up your home prior to moving? We've got you covered with our full service packing and unpacking services, too.</p>
  <div class="call abs">
    <span class="call-icon"><svg width="20" height="20" viewBox="0 0 24 24" fill="#fff"><path d="M6.6 10.8a15 15 0 006.6 6.6l2.2-2.2c.3-.3.7-.4 1-.2 1.1.4 2.3.6 3.6.6.6 0 1 .4 1 1V20c0 .6-.4 1-1 1A17 17 0 013 4c0-.6.4-1 1-1h3.5c.6 0 1 .4 1 1 0 1.3.2 2.5.6 3.6.1.3 0 .7-.2 1z"/></svg></span>
    Call us : (555) 014-2290
  </div>
</section>
<svg class="abs" style="left:0;top:1160px" width="1200" height="40" viewBox="0 0 1200 40"><path d="M0 0H1200V8C800 40 400 40 0 8Z" fill="#fff"/></svg>
<svg class="abs" style="left:0;top:1572px" width="1200" height="40" viewBox="0 0 1200 40"><path d="M0 40V30C400 0 800 0 1200 30V40Z" fill="#fff"/></svg>

<h2 class="section-title abs" style="top:1672px">What You Get</h2>
<p class="lead abs" style="top:1730px">When you partner with BOLT, you'll get the best service in the industry, as well as:<br><span class="perk-link">The Use of Packing &amp; Moving Materials:</span> The hourly rate includes the use of our dollies, ratchet straps, pads, moving tools, and property protection like floor mats, door-jamb protectors, stairwell protectors, and plenty of muscle!</p>

<div class="feature abs" style="left:112px;top:1850px">
  <div class="feature-ring"><div class="feature-art" role="img" aria-label="Icon of two movers carrying a box"></div></div>
  <h3>Trained, Licensed and<br>Insured Movers</h3>
  <p>All of our movers are highly trained to provide you with the best service, and to ensure the protection of you and your items.</p>
</div>
<div class="divider abs" style="left:424px"></div>
<div class="feature abs" style="left:450px;top:1850px">
  <div class="feature-ring"><div class="feature-art" role="img" aria-label="Icon of a professional team"></div></div>
  <h3>Professional</h3>
  <p>Honest, Uniformed, Nice, Knowledgeable Service is what you'll get with every member of our moving teams.</p>
</div>
<div class="divider abs" style="left:778px"></div>
<div class="feature abs" style="left:806px;top:1850px">
  <div class="feature-ring"><div class="feature-art" role="img" aria-label="Icon of a 24-hour phone line"></div></div>
  <h3>Custom Service for<br>Every Move</h3>
  <p>Every move is as unique as the person or business moving. Our training and equipment allows us to customize every project to ensure the very best for every client.</p>
</div>

<footer class="site-footer abs" role="img" aria-label="Darkened photo of a couple with moving boxes"></footer>
<svg class="footer-curve abs" width="1200" height="60" viewBox="0 0 1200 60">
  <path d="M0 0H1200V20C800 60 400 60 0 20Z" fill="#fff"/>
  <path d="M0 20C400 60 800 60 1200 20" fill="none" stroke="#8dc63f" stroke-width="6"/>
</svg>

<div class="newsletter abs">
  <h2>Subscribe to Newsletter</h2>
  <p>Sign up to hear from us about specials, packing tips, and more</p>
  <div class="subscribe-form"><span>Email Address</span><b>SUBSCRIBE</b></div>
</div>

<div class="footer-col abs" style="left:108px;top:2670px">
  <h4>Contact Us</h4>
  <div class="contact-row"><span class="ring-icon"><svg width="16" height="20" viewBox="0 0 16 22" fill="#fff"><path d="M8 0a8 8 0 00-8 8c0 6 8 14 8 14s8-8 8-14a8 8 0 00-8-8zm0 11a3 3 0 110-6 3 3 0 010 6z"/></svg></span><div>Bolt Hauling LLC<br>42 Larkin Ave., Fernbrook, MS 39000, US</div></div>
  <div class="contact-row"><span class="ring-icon"><svg width="18" height="18" viewBox="0 0 24 24" fill="#fff"><path d="M6.6 10.8a15 15 0 006.6 6.6l2.2-2.2c.3-.3.7-.4 1-.2 1.1.4 2.3.6 3.6.6.6 0 1 .4 1 1V20c0 .6-.4 1-1 1A17 17 0 013 4c0-.6.4-1 1-1h3.5c.6 0 1 .4 1 1 0 1.3.2 2.5.6 3.6.1.3 0 .7-.2 1z"/></svg></span><div>Call Today:<br>(555) 014-2290</div></div>
  <div class="contact-row"><span class="ring-icon"><svg width="20" height="14" viewBox="0 0 20 14" fill="#fff"><path d="M0 0h20v14H0zM2 2l8 6 8-6"/><path d="M1 1l9 7 9-7" fill="none" stroke="#2a1f18" stroke-width="1.5"/></svg></span><div>Email Us:<br>info@bolthaulingcrew.example</div></div>
</div>
<div class="footer-col abs" style="left:468px;top:2670px">
  <h4>Quick links</h4>
  <ul class="quick-links"><li>Home</li><li>About Us</li><li>Our Services</li><li>What You Get</li><li>Contact us</li></ul>
</div>
<div class="footer-col abs" style="left:670px;top:2670px"><h4>Get Directions</h4></div>
<div class="map abs" role="img" aria-label="Street map showing the office location"></div>

<div class="footer-rule abs"></div>
<p class="copyright abs">Copyright © 2017 Bolt Hauling LLC - All Rights Reserved.</p>
<div class="social-dot abs" aria-label="Social profile link"></div>

</body>
</html>
```